Business Card Design Competition

We need a business card design for our Internet Marketing company. We require both front and back designs and the final card must be 89x53mm in size, plus crop marks to 91x55mm. Colours as per logo, plus perhaps black and/or grey (#828282).
Final text must be editable (if you can supply an editable Fireworks PNG, even better)...
FRONT TEXT:
Full Name
Position
Address Line
Suburb, State, Postcode
Phone: 0000 000 000
Mobile: 0000 000 000
Email: xxx@brimleafpromo.com.au
Web: www.brimleafpromo.com.au
Rear of card should be a fresh design plus our slogan text: "Getting You Noticed" in large font, then in small text "Brimleaf Holdings Pty Ltd (ABN: 42 563 701 384)".
Target Market(s)
Small/Medium Businesses
Industry/Entity Type
Business
Look and feel
Each slider illustrates characteristics of the customer's brand and the style your logo design should communicate.

```html
<!DOCTYPE html>
<html lang="en">
<head>
<meta charset="utf-8">
<title>Brimleaf Promo – Business Card</title>
<link href="https://fonts.googleapis.com/css2?family=Open+Sans:wght@400;600;700&family=Michroma&display=swap" rel="stylesheet">
<style>
  :root {
    --page-bg: #e9e6e2;
    --card-dark: #2b2a2a;
    --card-mid: #3a3939;
    --orange: #f07d1a;
    --orange-light: #f7a823;
    --green: #7dc242;
    --green-light: #c9e59a;
    --white: #ffffff;
    --grey-text: #d8d8d8;
  }
  html, body {
    margin: 0;
    width: 1200px;
    height: 900px;
    overflow: hidden;
    background: var(--page-bg);
    font-family: "Open Sans", Arial, sans-serif;
  }
  .canvas {
    position: relative;
    width: 1200px;
    height: 900px;
  }
  .card {
    position: absolute;
    top: 290px;
    width: 545px;
    height: 312px;
    border-radius: 18px;
    overflow: hidden;
    background: radial-gradient(ellipse at 50% 35%, var(--card-mid) 0%, var(--card-dark) 70%);
    box-shadow: 0 4px 10px rgba(0,0,0,0.25);
  }
  .card--front { left: 38px; }
  .card--back { left: 620px; }
  .card__swoosh {
    position: absolute;
    left: 0; top: 0;
    width: 545px; height: 312px;
  }
  .brand {
    position: absolute;
    left: 28px;
    top: 92px;
    display: flex;
    align-items: center;
    gap: 12px;
  }
  .brand__dot {
    width: 46px; height: 46px;
    border-radius: 50%;
    background: var(--orange);
  }
  .brand__name {
    font-weight: 600;
    font-size: 27px;
    color: var(--orange);
    white-space: nowrap;
  }
  .contact {
    position: absolute;
    left: 322px;
    top: 52px;
    color: var(--white);
  }
  .contact__name {
    font-weight: 700;
    font-size: 17px;
    line-height: 1.1;
  }
  .contact__role {
    font-size: 10px;
    line-height: 13px;
    color: var(--grey-text);
    margin-bottom: 26px;
  }
  .contact__address {
    font-size: 11px;
    line-height: 16px;
    margin-bottom: 6px;
  }
  .contact__row {
    display: flex;
    align-items: center;
    gap: 8px;
    font-size: 11px;
    line-height: 16px;
  }
  .contact__row svg { width: 10px; height: 10px; flex: none; }
  .contact__gap { height: 10px; }
  .back-mark {
    position: absolute;
    left: 0; right: 0;
    top: 28px;
    display: flex;
    flex-direction: column;
    align-items: center;
    gap: 8px;
  }
  .back-mark__dot {
    width: 86px; height: 86px;
    border-radius: 50%;
    background: var(--green);
  }
  .back-mark__name {
    font-weight: 600;
    font-size: 20px;
    line-height: 26px;
    color: var(--orange);
  }
  .slogan {
    position: absolute;
    left: 0; right: 0;
    top: 180px;
    text-align: center;
    font-family: "Michroma", "Open Sans", sans-serif;
    font-size: 22px;
    line-height: 30px;
    letter-spacing: 2px;
    color: var(--white);
  }
  .company-line {
    position: absolute;
    left: 0; right: 0;
    top: 218px;
    text-align: center;
    font-family: Arial, "Open Sans", sans-serif;
    font-size: 11px;
    line-height: 14px;
    color: var(--white);
  }
</style>
</head>
<body>
<main class="canvas">

  <section class="card card--front" aria-label="Business card front">
    <svg class="card__swoosh" viewBox="0 0 545 312" aria-hidden="true">
      <path d="M0 240 C180 268 380 268 545 236 L545 312 L0 312 Z" fill="var(--orange)"/>
      <path d="M0 256 C180 282 380 282 545 250 L545 312 L0 312 Z" fill="var(--orange-light)"/>
      <path d="M0 272 C180 294 380 292 545 262 L545 267 C380 297 180 299 0 278 Z" fill="var(--green-light)"/>
    </svg>

    <div class="brand">
      <span class="brand__dot"></span>
      <span class="brand__name">Brimleaf Promo</span>
    </div>

    <div class="contact">
      <div class="contact__name">Liam Carver</div>
      <div class="contact__role">Company Director</div>
      <div class="contact__address">17 harwick lane, Millbrook<br>County Ashby HW12 4PL 5678</div>
      <div class="contact__row">
        <svg viewBox="0 0 10 10"><rect x="2.5" y="0.5" width="5" height="9" rx="1" fill="none" stroke="#fff"/><rect x="3.5" y="2" width="3" height="4" fill="#fff"/></svg>
        061-700-4812
      </div>
      <div class="contact__row">
        <svg viewBox="0 0 10 10"><path d="M1 3 Q5 0 9 3 L8 4.5 L6.5 3.8 L3.5 3.8 L2 4.5 Z M2.5 5 H7.5 L8.5 9 H1.5 Z" fill="#fff"/></svg>
        061-703-9260
      </div>
      <div class="contact__gap"></div>
      <div class="contact__row">
        <svg viewBox="0 0 10 10"><rect x="0.5" y="2" width="9" height="6" fill="none" stroke="#fff"/><path d="M0.5 2 L5 5.5 L9.5 2" fill="none" stroke="#fff"/></svg>
        liam@brimleafpromo.com.au
      </div>
      <div class="contact__row">
        <svg viewBox="0 0 10 10"><circle cx="5" cy="5" r="4.3" fill="none" stroke="#fff"/><path d="M0.7 5 H9.3 M5 0.7 C2.5 3 2.5 7 5 9.3 M5 0.7 C7.5 3 7.5 7 5 9.3" fill="none" stroke="#fff" stroke-width="0.8"/></svg>
        brimleafpromo.com.au
      </div>
    </div>
  </section>

  <section class="card card--back" aria-label="Business card back">
    <svg class="card__swoosh" viewBox="0 0 545 312" aria-hidden="true">
      <path d="M0 240 C180 264 370 264 545 236 L545 312 L0 312 Z" fill="var(--orange)"/>
      <path d="M0 256 C180 278 370 278 545 250 L545 312 L0 312 Z" fill="var(--orange-light)"/>
      <path d="M0 270 C180 290 370 290 545 262 L545 312 L0 312 Z" fill="var(--green)"/>
    </svg>

    <div class="back-mark">
      <span class="back-mark__dot"></span>
      <span class="back-mark__name">Brimleaf Promo</span>
    </div>

    <div class="slogan">Getting You Noticed</div>
    <div class="company-line">Brimleaf Holdings Pty Ltd (ABN: 42 563 701 384)</div>
  </section>

</main>
</body>
</html>
```